If everything digital fails, here's what to do

Hi, I would like a poster / infographic of a list of practical actions people could take in case the internet stops working. I've put together a list of 8 areas, with the situation for each, and the mitigation actions folks can take - I need it presented in a clear and aesthetically pleasing way. I will send you the file with the full text so you can include it all

General population, but likely people who are safety conscious and want to protect themselves and learn more about what to do to be tech literate and prepared

Tech / Cyber / Public safety / Civic tech

Sans Serif

• It's a lot of text, so I think the important thing is to have it all in one poster, or in a series of similar pages
• I would like it to be a bit brooding, but also elicit competence and that some experts have thought about this and it will all be okay
• I don't want it to look cartoonish, or cheap - less is more is sort of what I'm looking for

```html
<!DOCTYPE html>
<html lang="en">
<head>
<meta charset="utf-8">
<title>If Everything Digital Fails, Here's What To Do</title>
<link rel="stylesheet" href="https://fonts.googleapis.com/css2?family=Chakra+Petch:wght@600;700&family=Roboto+Condensed:wght@400;700&display=swap">
<style>
:root{
  --page:#ffffff;
  --ink:#1d1d28;
  --navy:#1b1744;
  --alert:#e0242c;
  --comms:#5b6cf2;
  --bank:#17b59d;
  --info:#f08a3e;
  --tech:#b34dd0;
  --trans:#2a9fe0;
  --glow:#ff4a5c;
}
*{box-sizing:border-box;margin:0;padding:0}
html,body{width:1200px;height:1200px;overflow:hidden;background:var(--page)}
.poster{
  position:absolute;left:30px;top:197px;width:934px;height:660px;
  transform:scale(1.2206);transform-origin:0 0;
  font-family:"Roboto Condensed",sans-serif;color:var(--ink);
}
.poster__backdrop{
  position:absolute;inset:0;
  background:
    radial-gradient(ellipse 42% 38% at 50% 22%, rgba(255,70,90,.35), transparent 70%),
    radial-gradient(ellipse 60% 50% at 50% 55%, #2c3a8e 0%, transparent 75%),
    linear-gradient(180deg,#241f5a 0%,#1b1744 60%,#191443 100%);
}
.hero-alert{position:absolute;left:402px;top:36px;width:122px;height:112px}
.headline{
  position:absolute;left:230px;top:180px;width:470px;text-align:center;
  font-family:"Chakra Petch",sans-serif;font-weight:700;font-size:25px;line-height:1.08;
  letter-spacing:1.2px;color:#fff;text-transform:uppercase;
  text-shadow:0 0 6px rgba(0,0,0,.6);
}
.headline em{font-style:normal;color:var(--glow)}

.card{
  position:absolute;background:#fff;width:210px;padding:6px 7px 7px;
  display:flex;flex-direction:column;
}
.card__head{
  position:relative;border-radius:6px;color:#fff;min-height:46px;
  display:flex;align-items:center;gap:6px;padding:5px 8px;
}
.card__icon{flex:none;width:32px;height:32px}
.card__title{font-family:"Chakra Petch",sans-serif;font-weight:700;font-size:13.5px;letter-spacing:.8px;line-height:1;text-transform:uppercase}
.card__sub{font-size:7px;line-height:1.15;margin-top:2px}
.badge{position:absolute;left:-4px;top:-5px;width:23px;height:21px}
.card__label{
  text-align:center;font-family:"Chakra Petch",sans-serif;font-weight:700;
  font-size:6.5px;letter-spacing:.8px;text-transform:uppercase;margin:6px 0 4px;
}
.card__box{
  flex:1;border:1.3px solid;border-radius:7px;padding:7px 8px;overflow:hidden;
  font-size:6.9px;line-height:1.3;
}
.card__box--dense{font-size:6.3px;line-height:1.28}
.steps{list-style:none}
.steps li{display:flex;gap:5px;margin-bottom:6px}
.steps .num{font-family:"Chakra Petch",sans-serif;font-weight:700;font-size:14px;line-height:1;width:9px;flex:none}
.steps b,.card__box b{font-weight:700}
.refresh{font-weight:700;text-decoration:underline}
.card__box p{margin-bottom:3px}

.card--comms .card__head{background:var(--comms)} .card--comms .card__label,.card--comms .num,.card--comms .refresh{color:var(--comms)} .card--comms .card__box{border-color:var(--comms)}
.card--bank .card__head{background:var(--bank)} .card--bank .card__label,.card--bank .refresh{color:var(--bank)} .card--bank .card__box{border-color:var(--bank)}
.card--info .card__head{background:var(--info)} .card--info .card__label,.card--info .refresh{color:var(--info)} .card--info .card__box{border-color:var(--info)}
.card--tech .card__head{background:var(--tech)} .card--tech .card__label,.card--tech .num,.card--tech .refresh{color:var(--tech)} .card--tech .card__box{border-color:var(--tech)}
.card--trans .card__head{background:var(--trans)} .card--trans .card__label,.card--trans .refresh{color:var(--trans)} .card--trans .card__box{border-color:var(--trans)}
.safety{color:var(--trans);font-weight:700;text-decoration:underline}
</style>
</head>
<body>
<svg width="0" height="0" style="position:absolute">
  <defs>
    <symbol id="alert-badge" viewBox="0 0 23 21">
      <path d="M11.5 1.5 L21.5 19.5 H1.5 Z" fill="#fff" stroke="#e0242c" stroke-width="2.4" stroke-linejoin="round"/>
      <rect x="10.4" y="7" width="2.2" height="7" fill="#e0242c"/>
      <rect x="10.4" y="15.2" width="2.2" height="2.2" fill="#e0242c"/>
    </symbol>
  </defs>
</svg>

<div class="poster">
  <div class="poster__backdrop" role="img" aria-label="Dark blue close-up of a glowing circuit board with a microchip"></div>

  <svg class="hero-alert" viewBox="0 0 95 90" aria-hidden="true">
    <path d="M47.5 6 L89 82 H6 Z" fill="none" stroke="#ff4a5c" stroke-width="6" stroke-linejoin="round"/>
    <rect x="43.5" y="30" width="8" height="30" rx="3" fill="#ff4a5c"/>
    <circle cx="47.5" cy="70" r="4.5" fill="#ff4a5c"/>
  </svg>

  <h1 class="headline">If everything digital <em>fails</em>,<br>here's what to do</h1>

  <section class="card card--comms" style="left:20px;top:15px;height:430px">
    <div class="card__head">
      <svg class="badge"><use href="#alert-badge"/></svg>
      <svg class="card__icon" viewBox="0 0 30 30" fill="none" stroke="#fff" stroke-width="1.6" stroke-linejoin="round">
        <rect x="13" y="3" width="12" height="18" rx="2"/><line x1="17" y1="18" x2="21" y2="18"/>
        <path d="M3 22 q0 -4 4 -4 h6 q4 0 4 4 v4 h-14 z"/><rect x="6" y="20" width="8" height="3"/>
      </svg>
      <div><div class="card__title">Communications</div><div class="card__sub">Cell phones / land-line phone services have stopped working</div></div>
    </div>
    <div class="card__label">Possible mitigations</div>
    <div class="card__box">
      <ol class="steps">
        <li><span class="num">1</span><span><b>Buy a two-way hand-held walkie talkie &amp; share the other with close friends.</b><br><span class="refresh">Refresh when?</span> Check to ensure your walkie talkie has working batteries every 12 months (and that you know / remember how the walkie talkie itself works)</span></li>
        <li><span class="num">2</span><span><b>Share a 'third space' safe spot with close contacts in town where you know you could meet in emergency situations if your home was not safe to remain in. Do the same with neighbours and folks who live in your neighbourhood - have a central gathering spot in your hood that you share with others so you can have a convening spot close by.</b><br><span class="refresh">Refresh when?</span> Have a quick reminder conversation about this with your close contacts every 12 months to ensure everyone knows that's the plan</span></li>
        <li><span class="num">3</span><span><b>Have a printed list of your close contacts' home addresses handy, if you don't know how to get to their places by heart.</b><br><span class="refresh">Refresh when?</span> Print a new such document every 12 months to ensure it stays up to date</span></li>
        <li><span class="num">4</span><span><b>Have a list of close contacts that might still have a working landline (ie. rotary, not voip-based), or who have a satellite phone</b><br><span class="refresh">Refresh when?</span> Remind yourself of this list and refresh it every 12 months or so</span></li>
        <li><span class="num">5</span><span><b>Make a list of the people in your life that you care about that may also be affected, and make sure you include individuals in your community that may be vulnerable in such a disruption (they may be older, may live alone, might need access to supply of medication).</b><br><span class="refresh">Refresh when?</span> Remind yourself of this list and refresh it every 12 months or so</span></li>
      </ol>
    </div>
  </section>

  <section class="card card--tech" style="left:707px;top:15px;height:430px">
    <div class="card__head">
      <svg class="badge"><use href="#alert-badge"/></svg>
      <svg class="card__icon" viewBox="0 0 30 30" fill="none" stroke="#fff" stroke-width="1.6" stroke-linejoin="round">
        <rect x="3" y="7" width="17" height="12" rx="1"/><line x1="1" y1="22" x2="22" y2="22"/>
        <rect x="20" y="10" width="8" height="13" rx="1.5"/>
      </svg>
      <div><div class="card__title">Tehnology</div><div class="card__sub">Computers (laptops, tablets, smart phones) have stopped working</div></div>
    </div>
    <div class="card__label">Possible mitigations</div>
    <div class="card__box">
      <ol class="steps">
        <li><span class="num">1</span><span><b>Save all important digital materials (e.g. photos) that don't also exist on paper on a portable hard drive. Remember to do this for all digital materials that have been saved to your cloud that you might have forgotten about (archived, etc.).</b><br><br><span class="refresh">Refresh when?</span> Do a backup and update every 6 months<br>Note: Since this is time-consuming, put a note in your calendar at the beginning of the year, choosing the time and date when you will do this (as noted in #5 above, you could do this in line with the solstice each year: June 20 and December 20)</span></li>
        <li><span class="num">2</span><span><b>Get a hand cranked radio to ensure you have access to important news and information about what's happening in your community (locally, as well as nationally/internationally).</b><br><span class="refresh">Refresh when?</span> Make sure the hand cranked radio has fresh batteries (change them every 12 months or so)</span></li>
        <li><span class="num">3</span><span><b>Download a copy of your city's maps (e.g. Wayfind Maps) on your phone for local access, and make sure you have a physical map in case you need to get somewhere new in your city in a rush, and you don't know how to get there.</b><br><span class="refresh">Refresh when?</span> N/A once done</span></li>
      </ol>
    </div>
  </section>

  <section class="card card--bank" style="left:248px;top:263px;height:178px">
    <div class="card__head">
      <svg class="badge"><use href="#alert-badge"/></svg>
      <svg class="card__icon" viewBox="0 0 30 30" fill="none" stroke="#fff" stroke-width="1.6" stroke-linejoin="round">
        <rect x="7" y="6" width="20" height="13" rx="1.5"/><rect x="3" y="10" width="20" height="13" rx="1.5" fill="#17b59d"/>
        <line x1="3" y1="14" x2="23" y2="14"/><line x1="6" y1="19" x2="12" y2="19"/>
      </svg>
      <div><div class="card__title">Banking</div><div class="card__sub">Debit and credit cards have stopped working (in stores; ATMs)</div></div>
    </div>
    <div class="card__label">Possible mitigations</div>
    <div class="card__box">
      <p><b>Have $500 in cash available in $20 bills.</b><br><span class="refresh">Refresh when?</span> N/A once done</p>
    </div>
  </section>

  <section class="card card--info" style="left:479px;top:263px;height:178px">
    <div class="card__head">
      <svg class="badge"><use href="#alert-badge"/></svg>
      <svg class="card__icon" viewBox="0 0 30 30" fill="none" stroke="#fff" stroke-width="1.6" stroke-linejoin="round">
        <path d="M10 12 v-4 a5 5 0 0 1 10 0 v4"/><rect x="6" y="12" width="18" height="14" rx="1.5"/>
        <circle cx="11" cy="20" r="1" fill="#fff"/><circle cx="15" cy="20" r="1" fill="#fff"/><circle cx="19" cy="20" r="1" fill="#fff"/>
      </svg>
      <div><div class="card__title">Information Management</div><div class="card__sub">Password manager services (cloud) have stopped working</div></div>
    </div>
    <div class="card__label">Possible mitigations</div>
    <div class="card__box">
      <p>Preamble: Many individuals don't remember their passwords anymore, having password managers generate complicated strings of characters as their passwords for their many digital accounts in their lives. <b>Print a full list of your accounts and their passwords and keep that document safely in your living space.</b><br><span class="refresh">Refresh when?</span> Print a new such document every 6 months to ensure the list remains up to date</p>
    </div>
  </section>

  <section class="card card--trans" style="left:20px;top:455px;height:195px">
    <div class="card__head">
      <svg class="badge"><use href="#alert-badge"/></svg>
      <svg class="card__icon" viewBox="0 0 30 30" fill="none" stroke="#fff" stroke-width="1.6" stroke-linejoin="round">
        <rect x="5" y="5" width="12" height="21" rx="1.5"/><rect x="8" y="8" width="6" height="5" fill="#fff"/>
        <path d="M17 12 h3 l3 3 v8 a2 2 0 0 0 4 0 v-11 l-3 -3"/>
      </svg>
      <div><div class="card__title">Transportations</div><div class="card__sub">Gas stations have stopped working</div></div>
    </div>
    <div class="card__label">Possible mitigations</div>
    <div class="card__box">
      <p><b>(If you own a car)<br>Have a standard 40L gas canister filled with gas and available close by in case needed.</b></p>
      <p><span class="refresh">Refresh when?</span> Use up the gas within 4 months or so, and refill the canister then (i.e. 3 times a year) so that it remains usable</p>
      <p><span class="safety">Safety note:</span> (If relevant) ensure the can is not in a place where kids can get to it, since it's not safe for kids to be around gas</p>
    </div>
  </section>

  <section class="card card--bank" style="left:248px;top:455px;height:195px">
    <div class="card__head">
      <svg class="badge"><use href="#alert-badge"/></svg>
      <svg class="card__icon" viewBox="0 0 30 30" fill="none" stroke="#fff" stroke-width="1.6" stroke-linejoin="round">
        <path d="M3 11 L15 4 L27 11 Z"/><line x1="7" y1="13" x2="7" y2="22"/><line x1="12" y1="13" x2="12" y2="22"/><line x1="18" y1="13" x2="18" y2="22"/><line x1="23" y1="13" x2="23" y2="22"/><line x1="3" y1="25" x2="27" y2="25"/>
      </svg>
      <div><div class="card__title">Banking</div><div class="card__sub">Debit and credit cards have stopped working; your bank can't access its own information (online)</div></div>
    </div>
    <div class="card__label">Possible mitigations</div>
    <div class="card__box card__box--dense">
      <p><b>Print paper records of your banking statements that prove what you have in your bank accounts and store it in a safe place in your living space.</b> Ensure it has dates showing and full amounts, as well as your identifiers (name and account numbers) as well as the institution itself (printed screenshots should work fine if your money is in a few accounts requiring many statements). Note the same goes for your liabilities (i.e. be able to prove how much you had left on your mortgage or other bigger loans, if you have such debt).<br><span class="refresh">Refresh when?</span> Update this document every 6-12 months</p>
    </div>
  </section>

  <section class="card card--info" style="left:479px;top:455px;height:195px">
    <div class="card__head">
      <svg class="badge"><use href="#alert-badge"/></svg>
      <svg class="card__icon" viewBox="0 0 30 30" fill="none" stroke="#fff" stroke-width="1.6" stroke-linejoin="round">
        <path d="M8 17 a5 5 0 0 1 1 -10 a6 6 0 0 1 11 1 a4.5 4.5 0 0 1 1 9 z"/><rect x="11" y="19" width="8" height="8" rx="1"/><line x1="15" y1="17" x2="15" y2="19"/>
      </svg>
      <div><div class="card__title">Information Management</div><div class="card__sub">Cloud storage services have stopped working</div></div>
    </div>
    <div class="card__label">Possible mitigations</div>
    <div class="card__box card__box--dense">
      <p><b>Do a backup of the important documents that are stored only in your cloud storage (e.g. that important email in your Corvane Mail; that tax document only issued digitally, etc.)</b><br><span class="refresh">Refresh when?</span> Do a backup and update every 6 months<br>Note: Since this is a time-consuming exercise but not necessarily the same exercise as #7 below, you could alternate the months when you do one versus the other. For example, you could do this with annual equinoxes: March 21 and Sept 21 (pro tip: star email messages that are important as they arrive, so that you know what needs to be backed up every six months; that way, you don't have to go searching through your whole inbox)</p>
    </div>
  </section>

  <section class="card card--tech" style="left:707px;top:455px;height:195px">
    <div class="card__head">
      <svg class="badge"><use href="#alert-badge"/></svg>
      <svg class="card__icon" viewBox="0 0 30 30" fill="none" stroke="#fff" stroke-width="1.6" stroke-linejoin="round">
        <path d="M3 14 L15 4 L27 14"/><path d="M6 12 v14 h18 v-14"/>
        <path d="M10 18 a7 7 0 0 1 10 0"/><path d="M12.5 21 a3.5 3.5 0 0 1 5 0"/><circle cx="15" cy="23.5" r=".8" fill="#fff"/>
      </svg>
      <div><div class="card__title">Tehnology</div><div class="card__sub">Smart home devices have stopped working</div></div>
    </div>
    <div class="card__label">Possible mitigations</div>
    <div class="card__box">
      <p><b>If you have a smart home device that needs to be connected to the internet to work and that doesn't have a manual override (e.g. a smart lock for your living space's main door, or for the garage) ensure you have a backup system in place that would not leave you stranded when the internet goes down.</b><br><span class="refresh">Refresh when:</span> N/A once done</p>
    </div>
  </section>
</div>
</body>
</html>
```